Modern business card design for professional copywriter

I'd like a business card design that I can use to have my cards printed out by plink.com as a squared corners business card (see artwork and design guidelines here: https://help.plink.com/hc/en-gb/sections/300481726-PLINK-Product-Templates)

The design should be clean and modern and reflect the colours, tone and branding on my website: https://noravestrel.com.au

Target Market(s)

Professionals, B2B small business owners

Industry/Entity Type

Business

Contact Information for Business Card

Nora Vestrel
m: 0427 593 864
e: nora@noravestrel.com.au
w: noravestrel.com.au

Font styles to use
Sans Serif

Requirements
Must have
• Tagline: "Smart copywriting for clever business people"
• Brand colours: fd8000, 009984, 666666 and black
Nice to have

```html
<!DOCTYPE html>
<html lang="en">
<head>
<meta charset="utf-8">
<title>Nora Vestrel – Business Card</title>
<link rel="stylesheet" href="https://fonts.googleapis.com/css2?family=Open+Sans:wght@400;600;700&display=swap">
<style>
  :root {
    --stage: #f2f2f2;
    --ink: #1a1616;
    --teal: #3c8b7a;
    --orange: #f08a1c;
    --white: #ffffff;
    --grey: #666666;
  }
  * { box-sizing: border-box; margin: 0; padding: 0; }
  html, body {
    width: 1200px; height: 533px; overflow: hidden;
    background: var(--stage);
    font-family: "Open Sans", Arial, sans-serif;
  }
  .stage { position: relative; width: 1200px; height: 533px; }
  .card {
    position: absolute; top: 87px;
    width: 544px; height: 309px;
    background: var(--teal);
    overflow: hidden;
  }
  .card--back { left: 60px; }
  .card--front { left: 620px; width: 541px; }
  .pattern { position: absolute; inset: 0; background: var(--teal); }
  .panel { position: absolute; top: 0; bottom: 0; background: var(--ink); }
  .card--back .panel { left: 0; width: 220px; }
  .card--front .panel { left: 157px; width: 226px; }

  .brand-name {
    position: absolute;
    font-weight: 600;
    color: var(--orange);
    white-space: nowrap;
    display: flex; align-items: center; gap: 6px;
  }
  .brand-name .mark { width: 9px; height: 9px; background: var(--teal); }
  .card--back .brand-name { left: 0; width: 220px; justify-content: center; top: 144px; font-size: 22px; }
  .card--front .brand-name { left: 157px; width: 226px; justify-content: center; top: 138px; font-size: 28px; }

  .tagline {
    position: absolute; left: 157px; width: 226px; top: 198px;
    text-align: center;
    font-size: 7.5px; font-weight: 600; letter-spacing: 0.2px;
    color: var(--orange); text-transform: uppercase;
  }

  .person { position: absolute; left: 340px; top: 48px; }
  .person__name { font-size: 10.5px; font-weight: 700; letter-spacing: 0.4px; text-transform: uppercase; }
  .person__first { color: var(--white); }
  .person__last { color: var(--ink); }
  .person__role { font-size: 8px; color: var(--white); margin-top: 3px; letter-spacing: 0.3px; }

  .contacts { position: absolute; left: 340px; top: 107px; list-style: none; }
  .contacts li {
    display: flex; align-items: center; height: 16px; margin-bottom: 22px;
    font-size: 8.5px; color: var(--white); letter-spacing: 0.4px; text-transform: uppercase;
  }
  .contacts .icon {
    width: 15px; height: 15px; background: var(--orange); margin-right: 26px;
    display: flex; align-items: center; justify-content: center;
  }
  .contacts svg { width: 10px; height: 10px; fill: var(--ink); }
</style>
</head>
<body>
<main class="stage">

  <section class="card card--back" aria-label="Card back with contact details">
    <div class="pattern" role="img" aria-label="Teal geometric star and diamond line pattern"></div>
    <div class="panel"></div>
    <div class="brand-name"><span class="mark"></span>Nora Vestrel</div>

    <div class="person">
      <p class="person__name"><span class="person__first">Nora</span> <span class="person__last">Vestrel</span></p>
      <p class="person__role">COPYWRITER</p>
    </div>

    <ul class="contacts">
      <li>
        <span class="icon"><svg viewBox="0 0 24 24"><path d="M6.6 10.8a15.2 15.2 0 0 0 6.6 6.6l2.2-2.2c.3-.3.7-.4 1-.2 1.1.4 2.3.6 3.6.6.6 0 1 .4 1 1V20c0 .6-.4 1-1 1A17 17 0 0 1 3 4c0-.6.4-1 1-1h3.5c.6 0 1 .4 1 1 0 1.3.2 2.5.6 3.6.1.3 0 .7-.2 1z"/></svg></span>
        0427 593 864
      </li>
      <li>
        <span class="icon"><svg viewBox="0 0 24 24"><path d="M2 5h20v14H2z M4 7v1l8 5 8-5V7l-8 5z" fill-rule="evenodd"/></svg></span>
        nora@noravestrel.com.au
      </li>
      <li>
        <span class="icon"><svg viewBox="0 0 24 24"><path d="M12 3 2 12h3v9h5v-6h4v6h5v-9h3z"/></svg></span>
        noravestrel.com.au
      </li>
    </ul>
  </section>

  <section class="card card--front" aria-label="Card front with name and tagline">
    <div class="pattern" role="img" aria-label="Teal geometric star and diamond line pattern"></div>
    <div class="panel"></div>
    <div class="brand-name"><span class="mark"></span>Nora Vestrel</div>
    <p class="tagline">Smart copywriting for clever business people</p>
  </section>

</main>
</body>
</html>
```